Business Card Design Project - 2 sided

We need a business card design for a card having one business on each side (ie. two businesses on one card). Would like a design that incorporates logo, tagline and normal fields (name, position, address, phone).

Would also like an allowance for small font text along the bottom (text to be determined, but less than 50 characters).

NB. Attached logo for Verbal Bridgeworks has two variations - either can be used.

www.verbalbridgeworks.com / www.kelpora.com

```html
<!DOCTYPE html>
<html lang="en">
<head>
<meta charset="utf-8">
<title>Two-sided Business Card</title>
<link rel="stylesheet" href="https://fonts.googleapis.com/css2?family=Open+Sans:ital,wght@0,400;0,600;1,700&display=swap">
<style>
  :root {
    --backdrop: #9b9b9b;
    --card-blue: #4893b1;
    --card-white: #ffffff;
    --ink-navy: #1f1b6b;
    --brand-blue: #2d7fb2;
    --accent-green: #5cc43a;
    --card-shadow: rgba(0, 0, 0, 0.45);
  }
  * { box-sizing: border-box; margin: 0; padding: 0; }
  html, body {
    width: 1200px;
    height: 1200px;
    overflow: hidden;
    background: var(--backdrop);
    font-family: "Open Sans", Arial, sans-serif;
  }
  .card {
    position: absolute;
    left: 210px;
    width: 780px;
    height: 444px;
    border-radius: 38px;
    overflow: hidden;
    box-shadow: 10px 12px 14px var(--card-shadow);
  }
  .card--front { top: 78px; background: var(--card-white); }
  .card--back  { top: 678px; background: var(--card-blue); }

  .band {
    position: absolute;
    left: 0;
    width: 100%;
    display: flex;
    align-items: center;
    justify-content: center;
    gap: 18px;
  }
  .card--front .band { top: 0; height: 233px; background: var(--card-blue); }
  .card--back .band  { top: 0; height: 195px; background: var(--card-white); }

  .brand-mark {
    width: 30px;
    height: 30px;
    border-radius: 50%;
  }
  .brand-name {
    font-weight: 600;
    font-size: 56px;
    letter-spacing: 1px;
  }
  .card--front .brand-mark { background: var(--accent-green); }
  .card--front .brand-name { color: var(--ink-navy); }
  .card--back .brand-mark { background: var(--accent-green); }
  .card--back .brand-name { color: var(--brand-blue); }

  .person {
    position: absolute;
    left: 90px;
    line-height: 1;
  }
  .card--front .person { top: 275px; color: var(--ink-navy); }
  .card--back .person  { top: 275px; color: var(--accent-green); }
  .person__name { font-size: 50px; font-weight: 400; }
  .person__role { font-size: 34px; margin-top: -4px; }

  .contacts {
    position: absolute;
    left: 412px;
    top: 276px;
    list-style: none;
    font-size: 22px;
    line-height: 26px;
  }
  .contacts li { display: flex; }
  .contacts__label {
    width: 46px;
    font-weight: 700;
    font-style: italic;
    color: var(--ink-navy);
  }
  .card--front .contacts__value { color: var(--ink-navy); }
  .card--back .contacts__value { color: var(--accent-green); }
</style>
</head>
<body>

<section class="card card--front">
  <div class="band">
    <span class="brand-mark"></span>
    <span class="brand-name">Verbal Bridgeworks</span>
  </div>
  <div class="person">
    <div class="person__name">John Doe</div>
    <div class="person__role">position</div>
  </div>
  <ul class="contacts">
    <li><span class="contacts__label">W:</span><span class="contacts__value">www.verbalbridgeworks.com</span></li>
    <li><span class="contacts__label">P:</span><span class="contacts__value">012345678</span></li>
    <li><span class="contacts__label">A:</span><span class="contacts__value">123 Rd My Address</span></li>
  </ul>
</section>

<section class="card card--back">
  <div class="band">
    <span class="brand-mark"></span>
    <span class="brand-name">Kelpora LLC</span>
  </div>
  <div class="person">
    <div class="person__name">John Doe</div>
    <div class="person__role">position</div>
  </div>
  <ul class="contacts">
    <li><span class="contacts__label">W:</span><span class="contacts__value">www.kelpora.com</span></li>
    <li><span class="contacts__label">P:</span><span class="contacts__value">012345678</span></li>
    <li><span class="contacts__label">A:</span><span class="contacts__value">123 Rd My Address</span></li>
  </ul>
</section>

</body>
</html>
```